Saffron Lantern Court Business Card

I am looking for a business card desgined for my restaurant. It is an Indian restaurant, we are looking for something thats modern, yet traditional with the indian culture, we are looking for colors that match our logo. The logo is a design of the building with the name of the restaurant. for more information on the restaurant go to www.saffronlanterncourt.example

Industry/Entity Type

Indian Restaurant

Contact Information for Business Card

we are looking for somthing thats modern, yet traditional with the indian culture, we are looking for colors that match our logo. The logo is a design of the building with the name of the restaurant. for more information on the restaurant go to www.saffronlanterncourt.example

Requirements
Must have
• The logo that is attached,
• Name: Harvinder Oberoi,
• address of the restaurant: 7328 West Larkspur Rd, Cedar Mesa, Arizona, 85099
• Phone: (602) 555-0147
• Fax: (602) 555-0193
• Restaurant Catering Banquet
• Website: www.SaffronLanternCourt.example
Nice to have
• wanted to get something that goes with the theme of the restaurant, which is traditional but also keep a very professional and modern touch

```html
<!DOCTYPE html>
<html lang="en">
<head>
<meta charset="utf-8">
<title>Saffron Lantern Court Business Card</title>
<link rel="stylesheet" href="https://fonts.googleapis.com/css2?family=Source+Sans+3:wght@400;600&display=swap">
<style>
  :root {
    --page-bg: #e8e4e0;
    --card-light: #fcebe3;
    --card-peach: #f2b08c;
    --band-red: #a3282a;
    --brand-red: #a8392a;
    --icon-orange: #e2772b;
    --ink: #2a2522;
    --white: #ffffff;
    --banquet-pink: #e0508a;
    --banquet-rose: #c9405e;
    --banquet-cream: #f1c8c0;
  }
  * { margin: 0; padding: 0; box-sizing: border-box; }
  html, body {
    width: 1200px; height: 992px; overflow: hidden;
    background: var(--page-bg);
    font-family: "Source Sans 3", sans-serif;
  }
  .business-card {
    position: absolute; left: 60px; top: 190px;
    width: 1080px; height: 611px;
    background: linear-gradient(90deg, var(--card-light) 35%, var(--card-peach) 100%);
    box-shadow: 0 6px 24px rgba(0,0,0,.18);
    overflow: hidden;
  }
  .banquet-photo { position: absolute; left: 0; top: 0; }
  .brand-name {
    position: absolute; left: 444px; top: 108px; width: 440px;
    text-align: center; color: var(--brand-red);
    font-weight: 600; font-size: 54px; line-height: 1.08;
    letter-spacing: 3px; text-transform: uppercase;
  }
  .contact-name {
    position: absolute; left: 540px; top: 352px;
    font-size: 30px; font-weight: 400; color: var(--ink);
  }
  .contact-list { position: absolute; left: 540px; top: 408px; list-style: none; }
  .contact-item {
    display: flex; align-items: center; height: 38px;
    font-size: 24px; color: var(--ink);
  }
  .contact-icon { width: 20px; height: 20px; margin-right: 15px; fill: var(--icon-orange); }
  .address-band {
    position: absolute; left: 0; bottom: 0; width: 100%; height: 73px;
    background: var(--band-red); color: var(--white);
    display: flex; align-items: center; justify-content: center;
    font-size: 24px; letter-spacing: .3px;
  }
  .address-band .contact-icon { margin-right: 10px; }
</style>
</head>
<body>
  <div class="business-card">
    <svg class="banquet-photo" width="380" height="538" viewBox="0 0 380 538" role="img" aria-label="Photo of the banquet hall with pink lighting and dressed tables">
      <defs>
        <linearGradient id="hallTone" x1="0" y1="0" x2="0" y2="1">
          <stop offset="0" stop-color="var(--banquet-pink)"/>
          <stop offset=".45" stop-color="var(--banquet-rose)"/>
          <stop offset="1" stop-color="var(--banquet-cream)"/>
        </linearGradient>
      </defs>
      <path d="M0 0 H305 C350 60 370 150 360 260 C352 360 325 450 320 538 H0 Z" fill="url(#hallTone)"/>
      <path d="M305 0 C350 60 370 150 360 260 C352 360 325 450 320 538" fill="none" stroke="var(--white)" stroke-width="6"/>
    </svg>

    <div class="brand-name">Saffron<br>Lantern<br>Court</div>

    <div class="contact-name">Harvinder Oberoi</div>
    <ul class="contact-list">
      <li class="contact-item">
        <svg class="contact-icon" viewBox="0 0 20 20" aria-hidden="true"><path d="M6 1h8a1.5 1.5 0 0 1 1.5 1.5v15A1.5 1.5 0 0 1 14 19H6a1.5 1.5 0 0 1-1.5-1.5v-15A1.5 1.5 0 0 1 6 1zm.5 2v12h7V3zm3.5 13a1 1 0 1 0 0 2 1 1 0 0 0 0-2z"/></svg>
        (602) 555-0147
      </li>
      <li class="contact-item">
        <svg class="contact-icon" viewBox="0 0 20 20" aria-hidden="true"><path d="M1 5h4v13H1zM6 7h13v11H6zm2 2v2h9V9zm0 4v1.5h2V13zm3.5 0v1.5h2V13zm3.5 0v1.5h2V13zM8 2h8v4H8z"/></svg>
        (602) 555-0193
      </li>
      <li class="contact-item">
        <svg class="contact-icon" viewBox="0 0 20 20" aria-hidden="true"><path d="M10 1a9 9 0 1 0 0 18 9 9 0 0 0 0-18zm-1 2.1V7H5.3A7 7 0 0 1 9 3.1zm2 0A7 7 0 0 1 14.7 7H11zM3.1 9H9v2H3.1a7 7 0 0 1 0-2zM11 9h5.9a7 7 0 0 1 0 2H11zM5.3 13H9v3.9A7 7 0 0 1 5.3 13zm5.7 0h3.7a7 7 0 0 1-3.7 3.9z"/></svg>
        www.SaffronLanternCourt.example
      </li>
    </ul>

    <div class="address-band">
      <svg class="contact-icon" viewBox="0 0 20 20" aria-hidden="true"><path d="M10 1a6 6 0 0 0-6 6c0 4.5 6 12 6 12s6-7.5 6-12a6 6 0 0 0-6-6zm0 8.5A2.5 2.5 0 1 1 10 4.5a2.5 2.5 0 0 1 0 5z"/></svg>
      7328 West Larkspur Rd, Cedar Mesa, Arizona, 85099
    </div>
  </div>
</body>
</html>
```